Simple, High-Class Web Design Wanted - Motivational Speakers Site

1. Full Brief/Request & Specs outlined on following video -
http://clipvane-recorder.com/watch/tbWrkLmQyP

2. Use colours, images as you feel suits objective (we are happy to pay up to US$30 for any good images but must have licence/permission).

3. Layout probably similar to existing site - www.podiumvoicehub.com.au / http://podiumvoicehub.com.au/contact.php

4. Must Be Able to Coded for MOBILE-FRIENDLINESS & WordPress friendly Ideal.

5. This is the first, small job of many we/graphic design jobs. If suits, winning designer may be offered all future work direct.

Thanks & look forward to your design. Glen.

Target Market(s)

corporates - high end

Number of Pages Required

2 page

Font styles to use
Sans Serif

Requirements
Must have
• Classy professional look
Nice to have
• all in Video in brief
Should not have
• too many images / new images I haven't approved

```html
<!DOCTYPE html>
<html lang="en">
<head>
<meta charset="utf-8">
<title>Podium Voice Hub – Find the perfect speaker</title>
<link href="https://fonts.googleapis.com/css2?family=Open+Sans:wght@300;400;600;700&display=swap" rel="stylesheet">
<style>
:root{
  --blue:#1f86d6;
  --blue-dark:#0f4f8c;
  --blue-deep:#0a3566;
  --orange:#f7941d;
  --grey-bg:#eef0f2;
  --grey-line:#d9dde1;
  --text:#6b7178;
  --text-dark:#3c4248;
  --icon-grey:#c9ced3;
  --white:#ffffff;
}
*{box-sizing:border-box;margin:0;padding:0}
html,body{width:1200px;height:2292px;overflow:hidden}
body{font-family:"Open Sans",Arial,sans-serif;color:var(--text);background:var(--white);position:relative}

/* header */
.hero{position:absolute;left:0;top:0;width:1200px;height:288px;overflow:hidden}
.hero-photo{position:absolute;inset:0;background:linear-gradient(180deg,#1d6fb8 0%,#2a8be0 55%,#1c6ab0 100%)}
.topbar{position:absolute;left:0;top:0;width:1200px;height:52px;display:flex;align-items:center;justify-content:space-between;padding:0 16px}
.brand{display:flex;align-items:center;gap:8px;color:var(--white);font-weight:700;font-size:15px;letter-spacing:.5px;text-transform:uppercase}
.brand-square{width:14px;height:14px;background:var(--white)}
.contact-mini{display:flex;gap:22px;font-size:13px;color:var(--white)}
.hero-lead{position:absolute;left:70px;top:70px;font-size:20px;font-weight:300;color:var(--white)}
.hero-lead strong{font-weight:700}
.btn{display:inline-block;background:var(--orange);color:var(--white);font-weight:700;text-transform:uppercase;letter-spacing:.5px;border-radius:3px}
.hero .btn{position:absolute;left:738px;top:146px;font-size:20px;padding:12px 26px}
.hero-sub{position:absolute;left:236px;top:212px;font-size:19px;font-weight:300;color:var(--white);line-height:1.45}
.hero-sub .wow{font-weight:700;font-size:24px}

/* intro */
.intro{position:absolute;left:0;top:288px;width:1200px;height:372px;background:var(--grey-bg)}
.intro-card{position:absolute;left:240px;top:90px;width:710px;height:256px;background:var(--white);border:1px solid var(--grey-line);padding:10px}
.video{position:absolute;left:10px;top:10px;width:360px;height:236px;background:linear-gradient(160deg,#cfd2d6,#9aa0a7)}
.video-bar{position:absolute;left:0;bottom:0;width:100%;height:26px;background:rgba(20,24,30,.85)}
.video-bar svg{position:absolute;left:8px;top:6px}
.video-track{position:absolute;left:34px;right:12px;top:12px;height:3px;background:#666}
.video-track i{display:block;width:18%;height:100%;background:var(--blue)}
.presenter{position:absolute;left:390px;top:12px;font-size:12px;color:var(--text-dark)}
.presenter b{font-weight:700}
.tags{position:absolute;left:390px;top:32px;display:flex;gap:4px}
.tag{background:var(--blue);color:var(--white);font-size:11px;padding:2px 6px}
.quote{position:absolute;left:390px;top:66px;width:300px;display:flex;gap:10px}
.quote-mark{font-size:60px;line-height:48px;color:var(--blue);font-weight:700}
.quote p{font-size:13px;line-height:1.5;color:var(--blue)}

/* about text */
.about{position:absolute;left:240px;top:690px;width:720px;font-size:13px;line-height:1.55}
.about p{margin-bottom:8px}
.criteria{margin:6px 0 8px 20px}
.criteria dt{font-weight:600;color:var(--text-dark)}
.criteria dd{margin:0 0 4px 56px}

/* call band */
.call-band{position:absolute;left:0;top:1120px;width:1200px;height:152px;background:linear-gradient(180deg,#1b74c4,#2a8be0 50%,#1b6fbd);display:flex;align-items:center;justify-content:center;gap:18px}
.call-band p{color:var(--white);font-size:20px;font-weight:600}
.call-band .btn{font-size:20px;padding:10px 22px}

/* note */
.note{position:absolute;left:0;top:1272px;width:1200px;height:320px;background:var(--white)}
.note-icon{position:absolute;left:248px;top:90px}
.note h2{position:absolute;left:380px;top:56px;font-size:17px;font-weight:600;color:var(--text-dark)}
.note p{position:absolute;left:380px;top:92px;width:580px;font-size:13px;line-height:1.6}

/* testimonials */
.reviews{position:absolute;left:0;top:1592px;width:1200px;height:320px;background:var(--grey-bg)}
.reviews h2{position:absolute;left:240px;top:30px;font-size:17px;font-weight:600;color:var(--text-dark)}
.reviews-card{position:absolute;left:240px;top:76px;width:710px;height:220px;background:var(--white);border:1px solid var(--grey-line)}
.review{position:absolute;display:flex;gap:12px;align-items:flex-start}
.avatar{width:64px;height:64px;border-radius:50%;background:linear-gradient(160deg,#d6c2b0,#8f7a6a);flex:none}
.review-name{font-size:12px;color:var(--blue);font-weight:600}
.review-text{font-size:12px;line-height:1.5}
.review-quote{position:absolute;left:372px;top:22px;width:320px;display:flex;gap:10px}
.review-quote p{font-size:12px;line-height:1.55}

/* contact */
.contact{position:absolute;left:0;top:1912px;width:1200px;height:328px;background:var(--white)}
.contact h2{position:absolute;left:0;width:1200px;top:40px;text-align:center;font-size:19px;font-weight:300;color:var(--text-dark)}
.ways{position:absolute;left:350px;top:96px;width:500px;display:flex;justify-content:space-between}
.way{width:120px;display:flex;flex-direction:column;align-items:center;gap:8px}
.way.is-active{color:var(--blue);font-weight:600;font-size:15px;text-align:center;line-height:1.25}

/* footer */
.footer{position:absolute;left:0;top:2240px;width:1200px;height:52px;background:var(--blue-deep);color:#9fb6cf;font-size:11px;display:flex;align-items:center;justify-content:center}
</style>
</head>
<body>

<header class="hero">
  <div class="hero-photo" role="img" aria-label="Conference audience in a presentation hall, tinted blue"></div>
  <div class="topbar">
    <div class="brand"><span class="brand-square"></span>Podium Voice Hub</div>
    <div class="contact-mini"><span>hello@podiumvoicehub.com.au</span><span>1300 42 71 09</span></div>
  </div>
  <p class="hero-lead">Find the perfect speaker for your next event here.. <strong>FREE</strong> industry service</p>
  <a class="btn">Get in touch</a>
  <p class="hero-sub">Looking for a top motivational or guest speaker,<br>MC, or industry expert to <span class="wow">"WOW"</span> your next event? Find them here.</p>
</header>

<section class="intro">
  <div class="intro-card">
    <div class="video" role="img" aria-label="Video still of the founder speaking to camera">
      <div class="video-bar">
        <svg width="14" height="14" viewBox="0 0 14 14"><path d="M2 1 L13 7 L2 13 Z" fill="#fff"/></svg>
        <div class="video-track"><i></i></div>
      </div>
    </div>
    <div class="presenter"><b>Glen Harlow</b> – founder &amp; speaker advisor</div>
    <div class="tags"><span class="tag">motivational speaking</span><span class="tag">motivational speakers</span></div>
    <div class="quote">
      <span class="quote-mark">“</span>
      <p>Hi, I am Glen, the owner of this service. My clients and the speakers I recommend have all been checked by me, so you can find the right person quickly. Watch this video and get in touch with me... Where are you looking for?</p>
    </div>
  </div>
</section>

<section class="about">
  <p>Podium Voice Hub is a free industry service designed to help people looking for speakers save precious time and frustration in finding the most suitable paid speaker for their event.</p>
  <p>Suggestions are given by Australian conference speaker Glen Harlow, who has presented around Australia for a number of years and is familiar with many of our top professional speakers. He is as well as the leading speaker bureaus.</p>
  <p>If you would like a hand finding some good speaker options, simply send us the details of your event with the type of presenter you are ideally after, e.g.</p>
  <dl class="criteria">
    <dt>Topic/Most:</dt><dd>Motivational, Entertaining, Keynote, MC etc.</dd>
    <dt>Topic Area:</dt><dd>Team Building, Leadership, Innovation, Health/Life Balance etc.</dd>
    <dt>Approximate Budget:</dt><dd>$1000, $2500, $5000, $7500+ etc.</dd>
    <dt>Location:</dt><dd>Sydney, Melbourne, Brisbane, Perth, Adelaide, Canberra etc.</dd>
  </dl>
  <p>and where we can, we will be happy to send you some speaker possibilities. Many trusted speakers bureaus or simply some thoughts on the best advice for you to look. Regards Glen.</p>
</section>

<section class="call-band">
  <p>Let Glen help you to find the perfect speaker for your event:</p>
  <a class="btn">Click here</a>
</section>

<section class="note">
  <svg class="note-icon" width="80" height="80" viewBox="0 0 80 80" aria-hidden="true">
    <circle cx="40" cy="40" r="38" fill="var(--blue)"/>
    <circle cx="40" cy="22" r="5" fill="#fff"/>
    <rect x="35" y="32" width="10" height="30" rx="2" fill="#fff"/>
  </svg>
  <h2>Please Note:</h2>
  <p>Any information you provide will ONLY ever be used to help with your specific enquiry. More than one hour per request goes into finding the right fit, so please share as much detail as you can about your event. This service is, and will remain, free of charge for clients. Speakers recommended are chosen on merit and we never pass your details on to third parties. Please understand that while Glen tries to respond quickly, during busy periods a reply may take up to 48 hours.</p>
</section>

<section class="reviews">
  <h2>What people say about speakers I recommended &amp; about this service</h2>
  <div class="reviews-card">
    <div class="review" style="left:20px;top:20px;width:330px">
      <div class="avatar" role="img" aria-label="Portrait photo of a client"></div>
      <div><div class="review-name">Clara Whitfield, HR Manager</div><div class="review-text">Glen was really helpful with our search for a motivational speaker.</div></div>
    </div>
    <div class="review" style="left:20px;top:120px;width:330px">
      <div><div class="review-name">Daniel Orme</div><div class="review-text">motivational speaker</div></div>
      <div class="avatar" role="img" aria-label="Portrait photo of a speaker"></div>
    </div>
    <div class="review-quote">
      <span class="quote-mark">“</span>
      <p>Thank you so much Glen for recommending the speakers. We were very pleased with how our event went, and I will certainly be in touch for our next conference. Thanks again, Clara.</p>
    </div>
  </div>
</section>

<section class="contact">
  <h2>There are 3 ways to get in touch with Glen...</h2>
  <div class="ways">
    <div class="way">
      <svg width="110" height="80" viewBox="0 0 110 80" aria-label="Email">
        <rect x="5" y="10" width="100" height="64" rx="4" fill="var(--icon-grey)"/>
        <path d="M5 14 L55 48 L105 14" fill="none" stroke="#fff" stroke-width="4"/>
      </svg>
    </div>
    <div class="way is-active">
      <svg width="80" height="140" viewBox="0 0 80 140" aria-label="Phone">
        <rect x="6" y="4" width="68" height="132" rx="10" fill="var(--blue)"/>
        <rect x="14" y="20" width="52" height="92" fill="#fff"/>
        <circle cx="40" cy="124" r="5" fill="#fff"/>
      </svg>
      <span>Phone<br>1300 42 71 09</span>
    </div>
    <div class="way">
      <svg width="90" height="110" viewBox="0 0 90 110" aria-label="Contact form">
        <rect x="8" y="4" width="74" height="100" rx="3" fill="var(--icon-grey)"/>
        <rect x="18" y="20" width="54" height="8" fill="#fff"/>
        <rect x="18" y="36" width="54" height="8" fill="#fff"/>
        <rect x="18" y="52" width="54" height="24" fill="#fff"/>
        <rect x="44" y="84" width="28" height="10" fill="#fff"/>
      </svg>
    </div>
  </div>
</section>

<footer class="footer">© 2015 podiumvoicehub.com.au – All rights reserved</footer>

</body>
</html>
```